NPG Job bank

Western Guild of Bracework Practitioners Needs a design for our orthodontist job bank.

We are in the process of redesigning our current job board. We would like to improve our current design, focusing on the landing page and possibly the search page. I have attached images of what we currently have in place right now.

The Landing page: Currently, I find the landing page too wordy, members get confused when using it, we need something that is easier for providers are seekers to use. Set up more user friendly. Maybe have a button for become provider and become seeker and then a modal pops up with process.. The final design for this page needs to be user friendly, organized and clean. If someone were coming to this page for the first time they would know how to become a provider.

The search page: I was thinking it would be best to have the search options on the left hand side opposed to how it is just in the middle now. all of the information currently shown on this page needs to be included. The search results need improvement on how they are displayed as well.

If you have any questions feel free to contact me.

Industry/Entity Type

Bank

Number of Pages Required

1 page

Colors
33a6d7
85cae6
0692cd

Requirements
Must have
• A Landing page that is well designed and that is made in the blue colors that are shown on the attached files of what our job bank currently looks like. I have also attached 3 photos that could be used for a masthead, but keep in mind these do not have to be used, you can use any photo you would like, these are just for your convenience.
Nice to have
• An improved search results page along with the Landing page

```html
<!DOCTYPE html>
<html lang="en">
<head>
<meta charset="utf-8">
<title>NPG Job Bank</title>
<link rel="stylesheet" href="https://fonts.googleapis.com/css2?family=Source+Sans+3:wght@300;400;600&display=swap">
<style>
:root{
  --blue:#0692cd;
  --blue-mid:#33a6d7;
  --blue-light:#85cae6;
  --blue-deep:#0b7fbb;
  --navy:#1d3f8f;
  --ink:#444;
  --muted:#666;
  --footer:#232323;
  --white:#fff;
}
*{box-sizing:border-box;margin:0;padding:0}
html,body{width:1200px;height:2314px;overflow:hidden;background:var(--white);font-family:"Source Sans 3",Arial,sans-serif;color:var(--ink)}
.page{position:relative;width:1200px;height:2314px}
.brand{position:absolute;left:86px;top:66px;display:flex;align-items:center;gap:18px}
.brand-square{width:130px;height:118px;background:var(--blue);border-radius:6px}
.brand-name{color:var(--navy);font-weight:400;font-size:30px;line-height:32px;width:330px}
.brand-name small{display:block;font-size:22px;line-height:24px}
.account{position:absolute;right:86px;top:86px;font-size:19px;color:var(--muted);letter-spacing:.5px}
.search{position:absolute;left:853px;top:134px;width:261px;height:36px;border:1px solid #ccc;font-size:15px;color:#888;padding:7px 12px;font-family:inherit}
.search svg{position:absolute;right:10px;top:9px}
.nav{position:absolute;left:0;top:221px;width:1200px;height:59px;background:linear-gradient(#1aa3dc,#0b86c4);display:flex;padding-left:86px}
.nav a{color:var(--white);text-decoration:none;font-size:18px;line-height:59px;padding:0 28px;border-right:1px solid rgba(0,0,0,.15)}
.nav a.active{background:var(--blue-mid)}
.hero{position:absolute;left:0;top:280px;width:1200px;height:570px;background:linear-gradient(100deg,#e9eef2 0%,#b9dcef 45%,#8cc8e8 70%,#d8ecf6 100%)}
.hero-arrow{position:absolute;top:508px;width:62px;height:62px;border-radius:50%;background:rgba(90,90,90,.55)}
.welcome{position:absolute;top:918px;width:1200px;text-align:center;font-size:36px;font-weight:300;color:#333}
.welcome span{color:var(--navy)}
.intro{position:absolute;left:99px;top:988px;width:1002px;text-align:center;font-size:14px;line-height:21px;color:var(--muted)}
.card{position:absolute;top:1155px;width:444px;height:686px;border-radius:8px;background:linear-gradient(#0a9ad6,#14a8e6 50%,#0891d2);color:var(--white);text-align:center;box-shadow:0 26px 22px -18px rgba(0,0,0,.4)}
.card h2{height:95px;line-height:95px;font-size:36px;font-weight:400;background:var(--blue-deep);border-radius:8px 8px 0 0}
.card .lead{margin-top:27px;font-size:23px}
.card ul{list-style:none;margin-top:24px}
.card li{font-size:22px;line-height:40px}
.card li.step{height:43px}
.card .chev{display:block;margin:0 auto;height:43px;padding-top:8px}
.card .cta{display:block;margin:16px auto 0;width:251px;height:49px;border:2px solid var(--white);font-size:22px;line-height:45px;color:var(--white);text-decoration:none}
.provider{left:122px}
.seeker{left:641px}
.newsletter-title{position:absolute;left:116px;top:1928px;font-size:43px;font-weight:300;color:#555}
.newsletter-input{position:absolute;left:595px;top:1933px;width:337px;height:50px;border:1px solid #999;font-size:15px;padding:14px 14px;color:#555}
.newsletter-btn{position:absolute;left:932px;top:1933px;width:153px;height:50px;background:var(--blue);color:var(--white);font-size:23px;line-height:50px;text-align:center}
.footer{position:absolute;left:0;top:2055px;width:1200px;height:259px;background:var(--footer);color:var(--white);text-align:center}
.social{position:absolute;top:49px;left:0;width:1200px;display:flex;justify-content:center;gap:18px}
.social span{width:60px;height:60px;border:2px solid #ccc;border-radius:50%}
.footer-links{position:absolute;top:152px;width:1200px;font-size:15px}
.copyright{position:absolute;top:188px;width:1200px;font-size:15px}
</style>
</head>
<body>
<div class="page">
  <div class="brand">
    <div class="brand-square"></div>
    <div class="brand-name"><small>Member</small>Western Guild of Bracework Practitioners</div>
  </div>
  <div class="account">JOIN &nbsp;|&nbsp; SIGN IN</div>
  <div class="search">Search..
    <svg width="16" height="16" viewBox="0 0 16 16"><circle cx="6.5" cy="6.5" r="5" fill="none" stroke="#999" stroke-width="2"/><line x1="10" y1="10" x2="15" y2="15" stroke="#999" stroke-width="2"/></svg>
  </div>
  <nav class="nav">
    <a class="active">MEETINGS &amp; EVENTS</a><a>EDUCATION</a><a>PRACTICE MANAGEMENT</a><a>PUBLICATIONS</a><a>LEGAL</a><a>COMMUNITIES</a>
  </nav>
  <div class="hero" role="img" aria-label="Smiling family of three in a bright orthodontic treatment room">
    <svg class="hero-arrow" style="left:84px" viewBox="0 0 62 62"><polyline points="35,20 24,31 35,42" fill="none" stroke="#fff" stroke-width="2"/></svg>
    <svg class="hero-arrow" style="left:1050px" viewBox="0 0 62 62"><polyline points="27,20 38,31 27,42" fill="none" stroke="#fff" stroke-width="2"/></svg>
  </div>
  <h1 class="welcome">Welcome To <span>Our Website</span></h1>
  <p class="intro">Typi non habent claritatem insitam; est usus legentis in iis qui facit eorum claritatem. Investigationes demonstraverunt lectores legere me lius quod ii legunt saepius. Claritas est etiam processus dynamicus, qui sequitur mutationem consuetudium lectorum. Mirum est notare quam littera gothica, quam nunc putamus parum claram, anteposuerit litterarum formas humanitatis per seacula quarta decima et quinta decima. Eodem modo typi, qui nunc nobis videntur parum clari, fiant sollemnes in futurum.</p>

  <section class="card provider">
    <h2>PROVIDER</h2>
    <p class="lead">Post an Oppurtunity or Search Resumes</p>
    <ul>
      <li>Request Access</li>
      <li class="step"><svg class="chev" width="22" height="20" viewBox="0 0 22 20"><polyline points="2,2 11,9 20,2" fill="none" stroke="#fff" stroke-width="2"/><polyline points="2,9 11,16 20,9" fill="none" stroke="#fff" stroke-width="2"/></svg></li>
      <li>Post Oppurtunity</li>
      <li class="step"><svg class="chev" width="22" height="20" viewBox="0 0 22 20"><polyline points="2,2 11,9 20,2" fill="none" stroke="#fff" stroke-width="2"/><polyline points="2,9 11,16 20,9" fill="none" stroke="#fff" stroke-width="2"/></svg></li>
      <li>Search the Resume Center</li>
      <li class="step"><svg class="chev" width="22" height="20" viewBox="0 0 22 20"><polyline points="2,2 11,9 20,2" fill="none" stroke="#fff" stroke-width="2"/><polyline points="2,9 11,16 20,9" fill="none" stroke="#fff" stroke-width="2"/></svg></li>
      <li>Access Your Oppurtunities</li>
      <li class="step"><svg class="chev" width="22" height="20" viewBox="0 0 22 20"><polyline points="2,2 11,9 20,2" fill="none" stroke="#fff" stroke-width="2"/><polyline points="2,9 11,16 20,9" fill="none" stroke="#fff" stroke-width="2"/></svg></li>
      <li>Frequently Asked Questions</li>
    </ul>
    <a class="cta">BECOME PROVIDER</a>
  </section>

  <section class="card seeker">
    <h2>SEEKER</h2>
    <p class="lead">Post an Oppurtunity or Search Resumes</p>
    <ul>
      <li>Request Access</li>
      <li class="step"><svg class="chev" width="22" height="20" viewBox="0 0 22 20"><polyline points="2,2 11,9 20,2" fill="none" stroke="#fff" stroke-width="2"/><polyline points="2,9 11,16 20,9" fill="none" stroke="#fff" stroke-width="2"/></svg></li>
      <li>Post Oppurtunity</li>
      <li class="step"><svg class="chev" width="22" height="20" viewBox="0 0 22 20"><polyline points="2,2 11,9 20,2" fill="none" stroke="#fff" stroke-width="2"/><polyline points="2,9 11,16 20,9" fill="none" stroke="#fff" stroke-width="2"/></svg></li>
      <li>Search the Resume Center</li>
      <li class="step"><svg class="chev" width="22" height="20" viewBox="0 0 22 20"><polyline points="2,2 11,9 20,2" fill="none" stroke="#fff" stroke-width="2"/><polyline points="2,9 11,16 20,9" fill="none" stroke="#fff" stroke-width="2"/></svg></li>
      <li>Access Your Oppurtunities</li>
      <li class="step"><svg class="chev" width="22" height="20" viewBox="0 0 22 20"><polyline points="2,2 11,9 20,2" fill="none" stroke="#fff" stroke-width="2"/><polyline points="2,9 11,16 20,9" fill="none" stroke="#fff" stroke-width="2"/></svg></li>
      <li>Frequently Asked Questions</li>
    </ul>
    <a class="cta">BECOME SEEKER</a>
  </section>

  <h3 class="newsletter-title">Signup for Newsletter</h3>
  <div class="newsletter-input">Enter the Email Id</div>
  <div class="newsletter-btn">SIGNUP</div>

  <footer class="footer">
    <div class="social"><span></span><span></span><span></span><span></span></div>
    <div class="footer-links">Home &nbsp;|&nbsp; Explore &nbsp;|&nbsp; NPG Member Directory &nbsp;|&nbsp; About &nbsp;|&nbsp; Contact</div>
    <div class="copyright">Copyright © 2013. All Rights Reserved.</div>
  </footer>
</div>
</body>
</html>
```